Editable PDF and PowerPoint template /form

We need a fully editable form/template in PDF and PowerPoint. I have done a mock up with detailed instructions but happy to provide more detail. This is going to be used in our strategic planning monitoring for partner companies that we manage. The editable text boxes get bigger and smaller depending on the content we put in there. People also need to be able to drop their logo into the documents easily.

```html
<!DOCTYPE html>
<html lang="en">
<head>
<meta charset="UTF-8">
<title>Strategic Initiative Status Report</title>
<link href="https://fonts.googleapis.com/css2?family=Carlito:wght@400;700&display=swap" rel="stylesheet">
<style>
  :root {
    --page-bg: #ffffff;
    --ink: #000000;
    --header-bg: #7f7f7f;
    --header-ink: #ffffff;
    --rule: #000000;
    --grid: #3a3a3a;
    --brag-blue: #4472c4;
    --brag-red: #ff0000;
    --brag-amber: #ed7d31;
    --brag-green: #00b050;
  }
  * { margin: 0; padding: 0; box-sizing: border-box; }
  html, body {
    width: 1200px; height: 675px; overflow: hidden;
    background: var(--page-bg);
    font-family: "Carlito", "Calibri", Arial, sans-serif;
    color: var(--ink);
  }
  .report { position: relative; width: 1200px; height: 675px; }

  .meta-label {
    position: absolute; top: 42px;
    font-size: 15.5px; font-weight: 700; letter-spacing: 0.1px;
  }
  .meta-business { left: 50px; }
  .meta-owner { left: 511px; }
  .meta-date { left: 946px; }

  .status-table {
    position: absolute; left: 40px; top: 78px;
    width: 1120px; border-collapse: collapse; table-layout: fixed;
  }
  .status-table th, .status-table td {
    border: 1px solid var(--grid);
  }
  .status-table th {
    height: 56px; background: var(--header-bg); color: var(--header-ink);
    font-size: 13.5px; font-weight: 700; text-align: center; vertical-align: middle;
    border-color: #5a5a5a;
  }
  .status-table td { height: 70.8px; }
  .col-initiative { width: 343px; }
  .col-timeline { width: 105px; }
  .col-rag { width: 99px; }
  .col-commentary { width: 295px; }
  .col-mitigation { width: 278px; }

  .brag-title {
    position: absolute; left: 39px; top: 574px;
    font-size: 12.5px; font-weight: 700;
  }
  .brag-rule {
    position: absolute; left: 131px; top: 591px; width: 1029px; height: 1px;
    background: var(--rule);
  }
  .brag-item { position: absolute; top: 605px; display: flex; align-items: center; }
  .brag-swatch { width: 30px; height: 30px; flex: none; }
  .brag-text {
    font-size: 13.5px; font-weight: 700; line-height: 17px;
  }
  .brag-complete { left: 44px; }
  .brag-complete .brag-swatch { background: var(--brag-blue); }
  .brag-complete .brag-text { color: var(--brag-blue); margin-left: 9px; }
  .brag-red { left: 300px; }
  .brag-red .brag-swatch { background: var(--brag-red); }
  .brag-red .brag-text { color: var(--brag-red); margin-left: 9px; }
  .brag-amber { left: 633px; }
  .brag-amber .brag-swatch { background: var(--brag-amber); }
  .brag-amber .brag-text { color: var(--brag-amber); margin-left: 9px; }
  .brag-green { left: 944px; }
  .brag-green .brag-swatch { background: var(--brag-green); }
  .brag-green .brag-text { color: var(--brag-green); margin-left: 9px; }
</style>
</head>
<body>
<main class="report">
  <div class="meta-label meta-business">BUSINESS NAME:</div>
  <div class="meta-label meta-owner">OWNER:</div>
  <div class="meta-label meta-date">DATE:</div>

  <table class="status-table">
    <colgroup>
      <col class="col-initiative"><col class="col-timeline"><col class="col-rag"><col class="col-commentary"><col class="col-mitigation">
    </colgroup>
    <thead>
      <tr>
        <th>STRATEGIC INITIATIVE/ACTIVITY</th>
        <th>TIMELINE</th>
        <th>RAG STATUS</th>
        <th>PROGRESS COMMENTARY</th>
        <th>IF AMBER/RED MITIGATION REQUIRED</th>
      </tr>
    </thead>
    <tbody>
      <tr><td></td><td></td><td></td><td></td><td></td></tr>
      <tr><td></td><td></td><td></td><td></td><td></td></tr>
      <tr><td></td><td></td><td></td><td></td><td></td></tr>
      <tr><td></td><td></td><td></td><td></td><td></td></tr>
      <tr><td></td><td></td><td></td><td></td><td></td></tr>
      <tr><td></td><td></td><td></td><td></td><td></td></tr>
    </tbody>
  </table>

  <div class="brag-title">BRAG KEY</div>
  <div class="brag-rule"></div>

  <div class="brag-item brag-complete"><span class="brag-swatch"></span><span class="brag-text">ACTIVITY COMPLETE</span></div>
  <div class="brag-item brag-red"><span class="brag-swatch"></span><span class="brag-text">NOT ON TRACK,<br>NEED SIGNIFICANT MITIGATION</span></div>
  <div class="brag-item brag-amber"><span class="brag-swatch"></span><span class="brag-text">ON TRACK BUT FLAGGING MAY<br>NEED FUTURE MITIGATION</span></div>
  <div class="brag-item brag-green"><span class="brag-swatch"></span><span class="brag-text">ON TRACK AND NO ISSUES</span></div>
</main>
</body>
</html>
```